verdant manor grounds simple classy business card design

my name is owen brackley and I run a gardening business aimed at high class verdant manor grounds. the business name is verdant manor grounds and our logo was designed on brief hive .My clientel are anything from residential homes to businesses. I take pride in my work and know that I offer a service like no other in my area.
The business card will be used to represent my business and I want it to be not only rememberable, but simplistic and modern. Eye catching too. Of course I would like it relatable to gardening and appealing to the correct clientel - those being garden enthusiasts, prestigious homes and businesses that are after top of the line gardening services like no other on the market.
I am not a typical lawn mowing business so I don't want a typical card design that represents that. The gardens I work with are generally million dollar properties with owners who are very garden proud looking for upkeep and guidance from me along with sometimes whole new garden designs. I want the business cards to show to my clients that I take pride, as they do, in their garden. And I want them to know from my card that I am a professional, qualified horticulturist offering them a top of the line service for life. I want them to refer my business on. I want them to look at my business card and see class and professionalism in a modern unique bold way.
The card should be simple with the possibility of the logo on the front being embossed/debossed and my details on the back the card should have a organic garden feel it's very important to me that it is absolutely perfect
I am also very open to ideas and suggestions so look forward to seeing the designs. the business logo has been supplied with this project and I want the card to be double sided

Contact info is
Owen Brackley - Managing Director / Horticulturist
Phone : 0481 562 907
Email: owenbrackley@verdantmanorgrounds.example.au

Target Market(s)

high class gardens residential and commercial

Industry/Entity Type

Gardener

Contact Information for Business Card

Contact info is
Phone : 0481 562 907

PLEASE MAKE CARD DOUBLE SIDED

Requirements
Must have
• organic simple classy modern feel
• must flow with the current logo that has been supplied with this project
• Double sided
• Must explain in a simple way that I deal with high end gardens and I'm a qualified horticulturist
Nice to have
• embossed debossed logo
Should not have
• shouldn't be to busy or cheap looking

```html
<!DOCTYPE html>
<html lang="en">
<head>
<meta charset="utf-8">
<title>Owen Brackley – Verdant Manor Grounds</title>
<link rel="stylesheet" href="https://fonts.googleapis.com/css2?family=Open+Sans:wght@400;600&display=swap">
<style>
  :root {
    --paper: #efefed;
    --paper-shade: #e4e4e2;
    --ink-strong: #4a4a4a;
    --ink-soft: #7a7a7a;
    --rule: #8a8a8a;
    --leaf: #5e9a4e;
    --leaf-deep: #4f8a41;
  }
  html, body {
    margin: 0;
    padding: 0;
    width: 1200px;
    height: 702px;
    overflow: hidden;
    background: var(--paper);
  }
  .card {
    position: relative;
    width: 1200px;
    height: 702px;
    overflow: hidden;
    background: radial-gradient(ellipse at 40% 45%, #f4f4f2 0%, var(--paper) 55%, var(--paper-shade) 100%);
    font-family: "Open Sans", Arial, sans-serif;
  }
  .tree-art {
    position: absolute;
    left: 727px;
    top: 40px;
    width: 473px;
    height: 662px;
  }
  .person {
    position: absolute;
    left: 88px;
    top: 348px;
  }
  .person-name {
    margin: 0;
    font-size: 51px;
    font-weight: 600;
    line-height: 1;
    color: var(--ink-strong);
    letter-spacing: 0.2px;
  }
  .person-role {
    margin: 16px 0 0;
    font-size: 26px;
    font-weight: 400;
    color: var(--ink-soft);
  }
  .divider {
    position: absolute;
    left: 88px;
    top: 484px;
    width: 572px;
    height: 0;
    border-top: 1.5px solid var(--rule);
  }
  .contact-list {
    position: absolute;
    left: 88px;
    top: 518px;
    margin: 0;
    padding: 0;
    list-style: none;
  }
  .contact-item {
    display: flex;
    align-items: center;
    height: 38px;
    margin-bottom: 12px;
    font-size: 26px;
    color: var(--ink-strong);
    white-space: nowrap;
  }
  .contact-icon {
    width: 30px;
    height: 32px;
    margin-right: 20px;
    flex: none;
  }
</style>
</head>
<body>
  <main class="card">
    <svg class="tree-art" viewBox="0 0 473 662" role="img" aria-label="Embossed green leafy tree illustration">
      <defs>
        <radialGradient id="canopy-tone" cx="50%" cy="40%" r="60%">
          <stop offset="0%" stop-color="var(--leaf)" stop-opacity="0.85"/>
          <stop offset="100%" stop-color="var(--leaf-deep)" stop-opacity="0.6"/>
        </radialGradient>
      </defs>
      <ellipse cx="290" cy="345" rx="290" ry="335" fill="url(#canopy-tone)"/>
    </svg>

    <section class="person">
      <h1 class="person-name">Owen Brackley</h1>
      <p class="person-role">Managing Director / Horticulturist</p>
    </section>

    <div class="divider"></div>

    <ul class="contact-list">
      <li class="contact-item">
        <svg class="contact-icon" viewBox="0 0 30 32" aria-hidden="true">
          <rect x="7" y="1" width="16" height="30" rx="3" fill="none" stroke="var(--ink-strong)" stroke-width="2.4"/>
          <line x1="7" y1="24" x2="23" y2="24" stroke="var(--ink-strong)" stroke-width="2"/>
          <circle cx="15" cy="27.5" r="1.3" fill="var(--ink-strong)"/>
        </svg>
        <span class="contact-text">0481 562 907</span>
      </li>
      <li class="contact-item">
        <svg class="contact-icon" viewBox="0 0 30 32" aria-hidden="true">
          <path d="M2 13 L15 4 L28 13 V29 H2 Z" fill="none" stroke="var(--ink-strong)" stroke-width="2" stroke-linejoin="round"/>
          <rect x="7" y="8" width="16" height="12" fill="var(--paper)" stroke="var(--ink-strong)" stroke-width="1.6"/>
          <line x1="10" y1="12" x2="20" y2="12" stroke="var(--ink-strong)" stroke-width="1.4"/>
          <line x1="10" y1="15.5" x2="20" y2="15.5" stroke="var(--ink-strong)" stroke-width="1.4"/>
          <path d="M2 13 L15 22 L28 13 M2 29 L12 20 M28 29 L18 20" fill="none" stroke="var(--ink-strong)" stroke-width="2" stroke-linejoin="round"/>
        </svg>
        <span class="contact-text">owenbrackley@verdantmanorgrounds.example.au</span>
      </li>
    </ul>
  </main>
</body>
</html>
```